Semi Permanent make up flyer

Hi

I will be sending a few thousand flyers dropped door to door in some very lovely parts of London.

The flyer must contain the following information;

New studio in Greenwich

Velline Arc trained technician - gold advanced level

Free consultation no obligation

Price List;
Eyebrow hair stroke: £325
Eyebrows 3D effect: £395
Microblading hair stroke: £330
Eyelash enhancement Top: £250
Eyelash enhancement Top & Bottom: £300
Lip blush: £450

Tel;……………….
Facebook: Odrelle Permanent Cosmetics
Instagram: Odrelle_Permanent_Cosmetics

Special introductory offers - available for a limited time only;
Like & share my page for 10% off any treatment
Refer a friend for £50 off each
Buy one treatment get 50% off another

I would like it to look clean, professional, expensive, and high end/luxury

I’m happy to make this a double sided print so I can have my logo on the front and the information on the back.

It must include my logo.

If you could use images of appealing women I think it would work best. Images have to have nice eyes, lips and brows. Weather you use entire face or features that is up to you.

Please show me a selection of different colour ways across the whole design. I personally feel softer tones would work. No black or bright colours.

I will be getting my new phone number in the next few days. I will let you know via messages what it is for you to add it in.

Any questions feel free to ask.

Target Market(s)

Women

Industry/Entity Type

Beauty Salon

Font styles to use
Sans Serif

Requirements
Must have
• Everything in Description
Nice to have
• The designers give their ideas. Im looking for input
Should not have
• Childish, cheap images or fonts. This is very high end so needs to look it

```html
<!DOCTYPE html>
<html lang="en">
<head>
<meta charset="utf-8">
<title>Odrelle Permanent Cosmetics – Flyer</title>
<link rel="stylesheet" href="https://fonts.googleapis.com/css2?family=Lato:wght@300;400&family=Playfair+Display:ital,wght@0,400;0,600;1,400&display=swap">
<style>
:root{
  --page:#f3f2f0;
  --taupe-dark:#7d776a;
  --taupe-mid:#a8a296;
  --taupe-light:#ecebe6;
  --silver:#d9d6cf;
  --ink:#57544d;
  --ink-soft:#6e6a62;
  --tan:#c79a74;
  --tan-text:#f6eee6;
  --gold:#c9a24a;
  --skin-light:#f1e2d7;
  --skin-mid:#e4c8b6;
  --skin-deep:#d2ab93;
  --front-text:#8d8a86;
}
*{box-sizing:border-box;margin:0;padding:0}
html,body{width:1200px;height:908px;overflow:hidden;background:var(--page)}
.stage{position:relative;width:1200px;height:908px}
.flyer{position:absolute;top:140px;width:440px;height:620px;overflow:hidden;box-shadow:0 14px 30px rgba(0,0,0,.12)}
.flyer--back{left:130px;background:radial-gradient(ellipse 70% 60% at 55% 42%,var(--taupe-light) 0%,#d3d0c7 55%,var(--taupe-mid) 85%,var(--taupe-dark) 100%);font-family:"Lato",sans-serif;color:var(--ink)}
.flyer--front{left:630px}
.rule{position:absolute;left:0;right:0;height:3px;border-top:1px solid var(--silver);border-bottom:1px solid var(--silver)}
.rule--top{top:36px}.rule--bottom{bottom:40px}
.brand-tab{position:absolute;left:50%;top:0;transform:translateX(-50%);width:84px;height:92px;background:#9c968b;display:flex;flex-direction:column;align-items:center;justify-content:flex-end;padding-bottom:12px;color:var(--taupe-light)}
.brand-tab__mark{width:18px;height:18px;border-radius:50%;background:var(--gold);margin-bottom:10px}
.brand-tab__name{font-size:11px;letter-spacing:4px}
.brand-tab__sub{font-size:5px;letter-spacing:1px;margin-top:2px}
.headline{position:absolute;top:104px;width:100%;text-align:center;font-weight:300;font-size:22px;color:var(--ink-soft)}
.band{display:inline-block;background:var(--tan);color:var(--tan-text);font-family:"Playfair Display",serif;font-size:11px;letter-spacing:2.5px;padding:3px 12px}
.level{position:absolute;top:138px;left:0;right:0;text-align:center}
.prices{position:absolute;top:170px;left:60px;right:50px;list-style:none}
.prices li{display:flex;justify-content:space-between;align-items:baseline;height:38px;font-weight:300;font-size:14px}
.price{font-family:"Playfair Display",serif;font-style:italic;font-size:19px}
.price sup{font-size:9px}
.consult{position:absolute;top:408px;width:100%;text-align:center;font-size:10px;font-style:italic;font-weight:300}
.offers{position:absolute;top:430px;left:40px;right:34px;height:112px;border:1px solid var(--silver);text-align:center;padding-top:10px}
.offers__note{font-size:11px;letter-spacing:.5px;margin-top:3px}
.offers__row{display:flex;justify-content:space-around;align-items:center;margin-top:14px;font-size:11px;line-height:1.2;text-align:right}
.offers__big{font-family:"Playfair Display",serif;font-size:24px;margin-left:4px;text-align:left}
.offers__big small{font-size:10px}
.contacts{position:absolute;bottom:50px;left:26px;right:26px;display:flex;justify-content:space-between;align-items:center;font-size:9px;color:#f2f0ea}
.contact{display:flex;align-items:center;gap:6px}
.contact__dot{width:18px;height:18px;border-radius:50%;border:1px solid #f2f0ea;display:flex;align-items:center;justify-content:center}
.front-photo{position:absolute;inset:0;background:radial-gradient(ellipse 55% 70% at 30% 40%,var(--skin-light) 0%,var(--skin-mid) 60%,var(--skin-deep) 100%)}
.front-brand{position:absolute;right:30px;top:380px;width:190px;text-align:center;font-family:"Lato",sans-serif}
.front-brand__mark{width:30px;height:30px;border-radius:50%;background:var(--gold);margin:0 auto 14px}
.front-brand__name{font-size:24px;letter-spacing:9px;color:var(--front-text);font-weight:300}
.front-brand__sub{font-size:10px;letter-spacing:2px;color:var(--front-text);margin-top:2px}
.front-brand__studio{display:inline-block;margin-top:10px;background:var(--tan);color:var(--tan-text);font-family:"Playfair Display",serif;font-size:18px;letter-spacing:3px;padding:2px 12px}
.front-brand__place{font-size:13px;letter-spacing:3px;color:var(--front-text);margin-top:4px}
</style>
</head>
<body>
<main class="stage">
  <section class="flyer flyer--back">
    <div class="rule rule--top"></div>
    <div class="brand-tab">
      <span class="brand-tab__mark"></span>
      <span class="brand-tab__name">ODRELLE</span>
      <span class="brand-tab__sub">PERMANENT COSMETICS</span>
    </div>
    <h1 class="headline">Velline Arc trained technician</h1>
    <div class="level"><span class="band">GOLD ADVANCED LEVEL</span></div>
    <ul class="prices">
      <li><span>Eyebrow hair stroke</span><span class="price"><sup>£</sup>325</span></li>
      <li><span>Microblading hair stroke</span><span class="price"><sup>£</sup>330</span></li>
      <li><span>Eyebrows 3D effect</span><span class="price"><sup>£</sup>395</span></li>
      <li><span>Eyelash enhancement Top</span><span class="price"><sup>£</sup>250</span></li>
      <li><span>Eyelash enhancement Top &amp; Bottom</span><span class="price"><sup>£</sup>300</span></li>
      <li><span>Lip blush</span><span class="price"><sup>£</sup>450</span></li>
    </ul>
    <p class="consult">Free consultation no obligation</p>
    <div class="offers">
      <span class="band">SPECIAL INTRODUCTORY OFFERS</span>
      <p class="offers__note">available for a limited time only</p>
      <div class="offers__row">
        <span>Buy one<br>treatment get</span><span class="offers__big">50<small>%off</small></span>
        <span>Refer a<br>friend for</span><span class="offers__big">£50<small>off</small></span>
        <span>Like &amp; share<br>my page for</span><span class="offers__big">10<small>%off</small></span>
      </div>
    </div>
    <div class="contacts">
      <div class="contact">
        <span class="contact__dot">
          <svg width="10" height="10" viewBox="0 0 24 24"><path fill="#f2f0ea" d="M6.6 10.8a15 15 0 0 0 6.6 6.6l2.2-2.2a1 1 0 0 1 1-.25 11.4 11.4 0 0 0 3.6.57 1 1 0 0 1 1 1V20a1 1 0 0 1-1 1A17 17 0 0 1 3 4a1 1 0 0 1 1-1h3.5a1 1 0 0 1 1 1c0 1.25.2 2.45.57 3.6a1 1 0 0 1-.25 1z"/></svg>
        </span>
        <span>0000-000000<br>0000-000000</span>
      </div>
      <div class="contact"><span class="contact__dot"></span><span>/Odrelle Permanent Cosmetics</span></div>
      <div class="contact"><span class="contact__dot"></span><span>/Odrelle_Permanent_Cosmetics</span></div>
    </div>
    <div class="rule rule--bottom"></div>
  </section>

  <section class="flyer flyer--front">
    <div class="front-photo" role="img" aria-label="Close-up beauty photograph of a woman with defined brows, blue eyes and red lips, hand at her chin, on a soft peach background"></div>
    <div class="front-brand">
      <div class="front-brand__mark"></div>
      <div class="front-brand__name">ODRELLE</div>
      <div class="front-brand__sub">PERMANENT COSMETICS</div>
      <div class="front-brand__studio">NEW STUDIO</div>
      <div class="front-brand__place">in Greenwich</div>
    </div>
  </section>
</main>
</body>
</html>
```